Webpage for a treatment housing for young addicts.

I need a new design and files for my wordpress page. I need it to be more neat and clean. I need it to look professional with a starting page that will work as a navigation. I need like logo and phone number and such up top, a picture under it with one sentence as a slogan and under it 6 boxes to click to come to our different pages. Under it I want news etc.

Target Market(s)

Social services, employees and governements

Coding

Coded - Design and coding required

Font styles to use
Sans Serif

Colors
abd037
3176b5
9d9d9d
aaaaaa
f04a50

Requirements
Must have
• A nice design
Nice to have
• need it to look professional with a starting page that will work as a navigation. I need like logo and phone number and such up top, a picture under it with one sentence as a slogan and under it 6 boxes to click to come to our different pages. Under it I want news etc.
• today www.kolrev.se
• want more like www.tralvik.se or www.bersona.se
Should not have
• To many different colours and a messy design.

```html
<!DOCTYPE html>
<html lang="sv">
<head>
<meta charset="utf-8">
<title>Kolrev – Omsorg Vård Boende</title>
<link rel="stylesheet" href="https://fonts.googleapis.com/css2?family=Josefin+Sans:wght@700&family=Montserrat:wght@400;500;600;700&display=swap">
<style>
:root{
  --green:#8dc63f;
  --blue:#1a56a8;
  --navy:#0e4f9e;
  --footer:#0b55a6;
  --light:#f0f0f0;
  --text:#222;
  --muted:#777;
  --black:#1e1e1e;
  --white:#fff;
  --icon-dark:rgba(28,36,62,.72);
  --icon-light:rgba(255,255,255,.2);
}
*{box-sizing:border-box;margin:0;padding:0}
html,body{width:1200px;height:2177px;overflow:hidden;background:var(--white)}
body{position:relative;font-family:'Montserrat',sans-serif;color:var(--text)}

/* header */
.site-header{position:absolute;top:0;left:0;width:1200px;height:88px;background:var(--white)}
.brand{position:absolute;left:208px;top:22px;display:flex;align-items:center;gap:10px}
.brand-dot{width:42px;height:42px;border-radius:50%;background:var(--green)}
.brand-name{font-weight:700;font-size:31px;color:var(--blue)}
.header-contact{position:absolute;left:445px;width:400px;top:14px;text-align:center;color:var(--blue)}
.header-contact .lead{font-size:17px;font-weight:500}
.header-contact .phone{font-size:17px;color:var(--green);font-weight:500;display:flex;justify-content:center;align-items:center;gap:6px}
.header-contact .more{font-size:11px;margin-top:4px;color:#2b7ac0}
.menu-toggle{position:absolute;left:972px;top:35px;width:27px}
.menu-toggle span{display:block;height:4px;background:#111;margin-bottom:5px;border-radius:2px}

/* hero */
.hero{position:absolute;top:88px;left:0;width:1200px;height:560px}
.hero-photo{position:absolute;inset:0;background:linear-gradient(180deg,#8a8a84 0%,#c8c6bc 25%,#b8b5aa 45%,#6f7b76 70%,#4d4a44 100%)}
.hero-curve{position:absolute;left:0;bottom:0;width:1200px;height:140px}
.hero-title{position:absolute;top:96px;left:0;width:1200px;text-align:center;font-family:'Josefin Sans',sans-serif;font-size:39px;letter-spacing:4px;line-height:46px;color:#1b1b1b}
.hero-text{position:absolute;top:194px;left:365px;width:470px;text-align:center;font-size:14px;line-height:1.3;font-weight:500;color:var(--blue)}
.btn-pill{display:inline-block;background:var(--navy);color:var(--white);border-radius:16px;font-size:13.5px;font-weight:500;text-align:center}
.hero .btn-pill{position:absolute;top:271px;left:543px;width:114px;height:29px;line-height:29px}

/* nav boxes */
.page-links{position:absolute;top:692px;left:316px;display:grid;grid-template-columns:repeat(3,145px);column-gap:67px;row-gap:20px}
.page-link{height:35px;border:2px solid #2b7ac0;color:#2b7ac0;font-size:14px;display:flex;align-items:center;justify-content:center}

/* news */
.news{position:absolute;top:827px;left:0;width:1200px;height:461px;background:var(--light)}
.section-title{text-align:center;color:var(--green);font-weight:600;font-size:21px;letter-spacing:3px}
.news .section-title{position:absolute;top:26px;width:100%}
.news-card{position:absolute;top:78px;width:250px}
.news-photo{height:171px}
.news-date{font-size:9.5px;color:var(--muted);margin-top:12px}
.news-title{font-size:11.5px;color:var(--green);font-weight:600;margin-top:1px;line-height:1.2}
.news-text{font-size:11.5px;line-height:1.3;margin-top:12px;text-align:justify}
.btn-green{display:inline-block;background:var(--green);color:var(--white);font-size:13.5px;font-weight:500;width:82px;height:29px;line-height:29px;text-align:center;border-radius:3px;margin-top:14px}

/* social */
.social .section-title{position:absolute;top:1310px;width:1200px}
.social-panel{position:absolute;top:1364px;height:276px;display:flex;flex-direction:column;align-items:center;justify-content:center;color:var(--white);padding-top:10px}
.social-circle{width:66px;height:66px;border-radius:50%;background:var(--icon-dark);display:flex;align-items:center;justify-content:center}
.social-handle{font-weight:700;font-size:20px;margin-top:10px}

/* jobs */
.jobs{position:absolute;top:1640px;left:0;width:1200px;height:275px;background:var(--light)}
.jobs .section-title{position:absolute;top:36px;width:100%}
.jobs-text{position:absolute;top:86px;left:272px;width:650px;text-align:center;font-size:15px;letter-spacing:1.3px;line-height:1.75}
.jobs .btn-pill{position:absolute;top:204px;left:545px;width:111px;height:35px;line-height:35px;border-radius:18px}

/* footer */
.site-footer{position:absolute;top:1915px;left:0;width:1200px;height:221px;background:var(--footer);color:var(--white)}
.footer-nav{position:absolute;left:200px;top:36px;list-style:none;font-size:14.5px;letter-spacing:2px;line-height:24.5px}
.footer-contact{position:absolute;left:476px;top:36px;font-size:13.5px;letter-spacing:1.5px}
.footer-contact dt{font-weight:700;display:flex;align-items:center;gap:7px}
.footer-contact dd{margin:0 0 8px 22px;line-height:20px}
.newsletter{position:absolute;left:718px;top:36px}
.newsletter h3{font-size:13.5px;font-weight:600}
.newsletter-form{display:flex;margin-top:18px}
.newsletter-input{width:204px;height:34px;background:var(--white);color:#aaa;font-size:11.5px;padding:9px 10px}
.newsletter-btn{width:78px;height:34px;background:#111;font-size:10.5px;display:flex;align-items:center;justify-content:center}
.footer-social{display:flex;gap:10px;margin-top:20px}
.footer-social span{width:22px;height:22px;border-radius:50%;background:var(--icon-light);display:flex;align-items:center;justify-content:center}
.bottom-bar{position:absolute;top:2136px;left:0;width:1200px;height:41px;background:var(--black);color:var(--white);font-size:13.5px}
.bottom-bar .copy{position:absolute;left:200px;top:11px}
.bottom-bar .legal{position:absolute;left:719px;top:11px}
</style>
</head>
<body>

<header class="site-header">
  <div class="brand"><span class="brand-dot"></span><span class="brand-name">Kolrev</span></div>
  <div class="header-contact">
    <div class="lead">Hitta behandling eller support</div>
    <div class="phone">
      <svg width="13" height="13" viewBox="0 0 24 24"><path fill="#1a56a8" d="M6.6 10.8a15 15 0 006.6 6.6l2.2-2.2a1 1 0 011-.25 11.4 11.4 0 003.6.6 1 1 0 011 1V20a1 1 0 01-1 1A17 17 0 013 4a1 1 0 011-1h3.5a1 1 0 011 1c0 1.25.2 2.45.6 3.6a1 1 0 01-.25 1z"/></svg>
      010-1847260
    </div>
    <div class="more">Mer kontaktuppgifter Kontakt</div>
  </div>
  <div class="menu-toggle" aria-label="Meny"><span></span><span></span><span></span></div>
</header>

<section class="hero">
  <div class="hero-photo" role="img" aria-label="Foto: vandrare med stav blickar ut över molnigt bergslandskap"></div>
  <svg class="hero-curve" viewBox="0 0 1200 140" preserveAspectRatio="none"><path d="M0 0 Q600 265 1200 0 L1200 140 L0 140 Z" fill="#fff"/></svg>
  <h1 class="hero-title">VI SKAPAR HÅLLBARA<br>VÄGAR TILL EN BÄTTRE</h1>
  <p class="hero-text">Kolrev Sverige AB bedriver vård och omsorg riktat mot personer i ålder 14-25 år. Vi är specialister på psykosocial- missbruks- och kriminalitetsproblem</p>
  <a class="btn-pill">Berätta mer</a>
</section>

<nav class="page-links">
  <a class="page-link">HVB</a>
  <a class="page-link">Stödboende</a>
  <a class="page-link">Oppenvård</a>
  <a class="page-link">Vår behandling</a>
  <a class="page-link">Om oss</a>
  <a class="page-link">Placering</a>
</nav>

<section class="news">
  <h2 class="section-title">Nyheter</h2>
  <article class="news-card" style="left:200px">
    <div class="news-photo" role="img" aria-label="Foto: händer som planterar i lerkrukor" style="background:linear-gradient(135deg,#3d3a33,#7a5a40 55%,#5a5248)"></div>
    <div class="news-date">21 december, 2018</div>
    <h3 class="news-title">Lindaröd en väg från missbruk</h3>
    <p class="news-text">Lorem ipsum dolor sit amet, consectetur adipisicing elit, sed do eiusmod tempor incididunt ut labore et dolore magna aliqua.</p>
    <a class="btn-green">Läs mer</a>
  </article>
  <article class="news-card" style="left:476px">
    <div class="news-photo" role="img" aria-label="Foto: hammare och spikar på träbord" style="background:linear-gradient(135deg,#2a2a28,#8c8272 55%,#4a463e)"></div>
    <div class="news-date">21 december, 2018</div>
    <h3 class="news-title">Kraft Tillsammans bygger nya gemens-<br>kaper</h3>
    <p class="news-text">Lorem ipsum dolor sit amet, consectetur adipisicing elit, sed do eiusmod tempor incididunt ut labore et dolore magna aliqua.</p>
    <a class="btn-green">Läs mer</a>
  </article>
  <article class="news-card" style="left:750px">
    <div class="news-photo" role="img" aria-label="Foto: verktygsvägg med skiftnycklar" style="background:linear-gradient(135deg,#1f3558,#41587a 55%,#25375a)"></div>
    <div class="news-date">21 december, 2018</div>
    <h3 class="news-title">Så här går det till att flytta hemifrån</h3>
    <p class="news-text">Lorem ipsum dolor sit amet, consectetur adipisicing elit, sed do eiusmod tempor incididunt ut labore et dolore magna aliqua.</p>
    <a class="btn-green">Läs mer</a>
  </article>
</section>

<section class="social">
  <h2 class="section-title">Kolrev på social medier</h2>
  <div class="social-panel" style="left:0;width:399px;background:linear-gradient(160deg,#8f9ab8,#4f5c80)" role="img" aria-label="Foto: grupp unga som lägger händerna ihop">
    <span class="social-circle">
      <svg width="32" height="32" viewBox="0 0 24 24" fill="#fff"><circle cx="9" cy="8" r="3.2"/><circle cx="16.5" cy="9" r="2.6"/><path d="M2.5 19c0-3.6 2.9-6 6.5-6s6.5 2.4 6.5 6z"/><path d="M16.8 19c0-2-.6-3.7-1.7-4.9.4-.1.9-.1 1.4-.1 2.9 0 5 2 5 5z"/></svg>
    </span>
    <span class="social-handle">/kolrev.se</span>
  </div>
  <div class="social-panel" style="left:399px;width:403px;background:linear-gradient(160deg,#6fa7dc,#3d78b8)" role="img" aria-label="Foto: personer samtalar vid ett bord">
    <span class="social-circle">
      <svg width="30" height="30" viewBox="0 0 24 24" fill="#fff"><path d="M3 4h18a1 1 0 011 1v11a1 1 0 01-1 1H9l-5 4v-4H3a1 1 0 01-1-1V5a1 1 0 011-1z"/></svg>
    </span>
    <span class="social-handle">@kolrev.se</span>
  </div>
  <div class="social-panel" style="left:802px;width:398px;background:linear-gradient(160deg,#c9c4bc,#8c7a6c)" role="img" aria-label="Foto: publik som sitter och lyssnar">
    <span class="social-circle">
      <svg width="30" height="30" viewBox="0 0 24 24" fill="#fff"><circle cx="18" cy="5" r="3"/><circle cx="6" cy="12" r="3"/><circle cx="18" cy="19" r="3"/><path d="M8.6 10.7l6.8-4M8.6 13.3l6.8 4" stroke="#fff" stroke-width="2"/></svg>
    </span>
    <span class="social-handle">@kolrev.se</span>
  </div>
</section>

<section class="jobs">
  <h2 class="section-title">Jobba hos oss</h2>
  <p class="jobs-text">Ut enim ad minim veniam, quis nostrud exercitation ullamco laboris nisi ut aliquip ex ea commodo consequat. Duis aute irure dolor in reprehen-derit in voluptate velit esse cillum dolore eu fugiat nulla pariatur.</p>
  <a class="btn-pill">Läs mer</a>
</section>

<footer class="site-footer">
  <ul class="footer-nav">
    <li>Hem</li><li>Om Kolrev</li><li>Björkhagen HVB</li><li>Jobba hos oss</li><li>Behandling</li><li>Kontakt</li>
  </ul>
  <dl class="footer-contact">
    <dt><svg width="13" height="13" viewBox="0 0 24 24"><path fill="#fff" d="M6.6 10.8a15 15 0 006.6 6.6l2.2-2.2a1 1 0 011-.25 11.4 11.4 0 003.6.6 1 1 0 011 1V20a1 1 0 01-1 1A17 17 0 013 4a1 1 0 011-1h3.5a1 1 0 011 1c0 1.25.2 2.45.6 3.6a1 1 0 01-.25 1z"/></svg>Telefon</dt>
    <dd>010-1847260</dd>
    <dt><svg width="13" height="13" viewBox="0 0 24 24"><circle cx="12" cy="12" r="10" fill="none" stroke="#fff" stroke-width="2"/><path d="M12 6v6l4 2" fill="none" stroke="#fff" stroke-width="2"/></svg>Tidtabell</dt>
    <dd>Måndag - Fredag<br>09:00 - 18:00</dd>
    <dt><svg width="13" height="13" viewBox="0 0 24 24"><path fill="#fff" d="M2 5h20v14H2z"/><path d="M2 5l10 8 10-8" fill="none" stroke="#0b55a6" stroke-width="2"/></svg>E-post</dt>
    <dd>info@kolrev.se</dd>
  </dl>
  <div class="newsletter">
    <h3>Prenumerera på vårt nyhetsbrev</h3>
    <div class="newsletter-form"><div class="newsletter-input">E-post</div><div class="newsletter-btn">SUBSCRIBE</div></div>
    <div class="footer-social">
      <span><svg width="12" height="12" viewBox="0 0 24 24" fill="#fff"><circle cx="9" cy="8" r="3.5"/><path d="M2 20c0-4 3-6.5 7-6.5s7 2.5 7 6.5z"/><circle cx="17" cy="9" r="2.8"/></svg></span>
      <span><svg width="12" height="12" viewBox="0 0 24 24" fill="#fff"><path d="M3 4h18v12H9l-5 4v-4H3z"/></svg></span>
      <span><svg width="12" height="12" viewBox="0 0 24 24" fill="#fff"><circle cx="18" cy="5" r="3"/><circle cx="6" cy="12" r="3"/><circle cx="18" cy="19" r="3"/><path d="M8.6 10.7l6.8-4M8.6 13.3l6.8 4" stroke="#fff" stroke-width="2"/></svg></span>
      <span><svg width="12" height="12" viewBox="0 0 24 24" fill="#fff"><path d="M12 21l-8.5-8.6A5 5 0 0112 5.6a5 5 0 018.5 6.8z"/></svg></span>
      <span><svg width="12" height="12" viewBox="0 0 24 24" fill="none" stroke="#fff" stroke-width="2.6"><path d="M10 14a4 4 0 005.7 0l3-3a4 4 0 00-5.7-5.7l-1 1"/><path d="M14 10a4 4 0 00-5.7 0l-3 3a4 4 0 005.7 5.7l1-1"/></svg></span>
    </div>
  </div>
</footer>
<div class="bottom-bar">
  <span class="copy">Copyrigth 2018 Kolrev AB</span>
  <span class="legal">Personuppgifter – Tillgänglighet – Cookies</span>
</div>

</body>
</html>
```